Online video and marketing company business cards

Need to get some new business cards designed to fit with our new logo. The cards should be professional, clean and simple.

Cards should have:

Name
Position
2 line address
telephone
mobile
email address
web address

We need to have our logo and if possible say what we do...
ONLINE FILM PRODUCTION & STRATEGY

Marketing

```html
<!DOCTYPE html>
<html lang="en">
<head>
<meta charset="utf-8">
<title>lumenreel business cards</title>
<link href="https://fonts.googleapis.com/css2?family=Source+Sans+3:wght@400;600;700&display=swap" rel="stylesheet">
<style>
  :root {
    --page: #e9e7e4;
    --navy: #2a5275;
    --teal: #3a9bb5;
    --ink: #3c3c3c;
    --paper: #ffffff;
  }
  * { box-sizing: border-box; margin: 0; padding: 0; }
  html, body {
    width: 1200px; height: 997px; overflow: hidden;
    background: var(--page);
    font-family: "Source Sans 3", Arial, sans-serif;
  }
  .sheet {
    width: 1200px; height: 997px;
    display: flex; flex-direction: column; align-items: center; justify-content: center;
    gap: 60px;
  }
  .card {
    position: relative; width: 700px; height: 400px; overflow: hidden;
    box-shadow: 0 2px 6px rgba(0,0,0,.12);
  }

  /* back side */
  .card--back { background: var(--navy); }
  .card--back .brand {
    position: absolute; left: 70px; top: 140px;
    display: flex; align-items: center; gap: 24px;
  }
  .card--back .brand-mark { width: 64px; height: 64px; background: var(--paper); }
  .card--back .brand-name { font-size: 84px; font-weight: 700; color: var(--paper); line-height: .9; letter-spacing: -1px; }
  .card--back .brand-tagline { font-size: 15px; font-weight: 600; color: var(--paper); letter-spacing: .5px; margin-top: 10px; }

  /* front side */
  .card--front { background: var(--paper); }
  .card--front .brand {
    position: absolute; left: 48px; top: 150px;
    display: flex; align-items: center; gap: 12px;
  }
  .card--front .brand-mark { width: 30px; height: 30px; background: var(--navy); }
  .card--front .brand-name { font-size: 46px; font-weight: 700; color: var(--teal); line-height: .9; letter-spacing: -.5px; }
  .card--front .brand-tagline { font-size: 11px; font-weight: 600; color: var(--teal); letter-spacing: .4px; margin-top: 5px; }

  .person {
    position: absolute; right: 60px; top: 66px; text-align: right;
  }
  .person-name { font-size: 34px; font-weight: 400; color: var(--ink); line-height: 1.1; }
  .person-role { font-size: 18px; color: var(--ink); margin-top: 2px; }

  .contact {
    position: absolute; left: 48px; bottom: 40px; list-style: none;
    font-size: 15px; color: var(--ink); line-height: 24px;
  }
  .contact li { display: flex; align-items: center; gap: 8px; }
  .contact svg { width: 13px; height: 13px; fill: var(--ink); flex: none; }
</style>
</head>
<body>
<main class="sheet">
  <section class="card card--back">
    <div class="brand">
      <span class="brand-mark"></span>
      <div>
        <div class="brand-name">lumenreel</div>
        <div class="brand-tagline">ONLINE FILM PRODUCTION &amp; STRATEGY</div>
      </div>
    </div>
  </section>

  <section class="card card--front">
    <div class="person">
      <div class="person-name">Marcus Hale</div>
      <div class="person-role">Executive</div>
    </div>
    <div class="brand">
      <span class="brand-mark"></span>
      <div>
        <div class="brand-name">lumenreel</div>
        <div class="brand-tagline">ONLINE FILM PRODUCTION &amp; STRATEGY</div>
      </div>
    </div>
    <ul class="contact">
      <li><svg viewBox="0 0 16 16"><path d="M8 1 0 8h2v7h4v-5h4v5h4V8h2z"/></svg>418 Birchwood Lane, Carver, Ontario</li>
      <li><svg viewBox="0 0 16 16"><path d="M0 3h16v10H0z"/><path d="M1 4l7 5 7-5" fill="none" stroke="#ffffff" stroke-width="1.2"/></svg>sales@lumenreel.com</li>
      <li><svg viewBox="0 0 16 16"><path d="M1 5c0-2 2-3 7-3s7 1 7 3v2h-4V5H5v2H1zM3 8h10l2 6H1z"/></svg>001 0842 36 17 58</li>
      <li><svg viewBox="0 0 16 16"><path d="M4 0h8v16H4zM5 2v10h6V2z" fill-rule="evenodd"/></svg>001 0842 36 17 58</li>
      <li><svg viewBox="0 0 16 16"><circle cx="8" cy="8" r="7" fill="none" stroke="#3c3c3c" stroke-width="1.5"/><path d="M1 8h14M8 1c-3 4-3 10 0 14M8 1c3 4 3 10 0 14" fill="none" stroke="#3c3c3c" stroke-width="1.2"/></svg>lumenreel.com</li>
    </ul>
  </section>
</main>
</body>
</html>
```